Flyer for Pharmacy/Medical Convention

Tri-fold flyer for pharmacy/medical convention. The inside of the flyer we would like to look like a venn diagram, possibly using an image similar to our blue logo

Copy write will be submitted when a design is chosen

there will be a flap about educational features, one about supplements an automated recommendations, and a flap about a computer platform to manage patients

Target Market(s)

Pharmacists and Medical Providers

Industry/Entity Type

Supplement

Colors

Designer to choose colors to be used in the design.

Requirements
Must have
• color scheme similar to logos and or label design attached

```html
<!DOCTYPE html>
<html lang="en">
<head>
<meta charset="utf-8">
<title>Vitalis Wellness Solutions – Tri-fold Flyer</title>
<link href="https://fonts.googleapis.com/css2?family=Poppins:wght@400;500;600;700&family=Open+Sans:wght@400;600&family=Roboto+Condensed:wght@400;700&family=Libre+Baskerville:wght@700&display=swap" rel="stylesheet">
<style>
  :root{
    --navy:#232a86;
    --blue:#1d5fb8;
    --bright:#1a78c9;
    --dark:#333436;
    --paper:#f5f5f7;
    --grey:#e2e2e6;
    --text:#3b3b3f;
    --yellow:#ffe93a;
    --white:#ffffff;
  }
  *{box-sizing:border-box;margin:0;padding:0}
  html,body{width:1200px;height:970px;overflow:hidden;background:var(--paper)}
  .flyer{position:relative;width:1200px;height:970px}
  .flyer-bg{position:absolute;left:0;top:0;width:1200px;height:970px}
  .panel{position:absolute;top:0;width:400px;height:970px}
  .panel-left{left:0}
  .panel-middle{left:400px}
  .panel-right{left:800px}

  /* left flap */
  .platform-intro{position:absolute;left:42px;top:58px;width:320px;font-family:"Open Sans",sans-serif;color:var(--text)}
  .platform-title{font-family:"Poppins",sans-serif;font-weight:700;font-size:27px;color:var(--navy);line-height:1.1}
  .platform-sub{font-family:"Poppins",sans-serif;font-size:17px;color:var(--text);letter-spacing:.3px}
  .title-rule{width:62px;height:3px;background:var(--navy);margin:6px 0 10px}
  .platform-copy{font-size:13.5px;line-height:1.35}
  .feature{position:relative;margin-top:14px;padding-left:22px;font-size:13.5px;line-height:1.35}
  .feature::before{content:"";position:absolute;left:2px;top:6px;width:9px;height:9px;border-radius:50%;background:var(--navy)}
  .feature-title{display:block;font-family:"Poppins",sans-serif;font-weight:500;color:var(--navy);font-size:14px}
  .gap-callout{position:absolute;left:81px;top:378px;width:250px;text-align:center;font-family:"Poppins",sans-serif;color:var(--white);font-size:24px;line-height:1.25}
  .gap-callout strong{color:var(--yellow);font-weight:700}

  /* brand + contact */
  .brand{position:absolute;font-family:"Poppins",sans-serif;font-weight:700;color:var(--navy);line-height:1.25}
  .brand-name{font-size:26px;letter-spacing:1px}
  .brand-sub{display:block;font-family:"Libre Baskerville",serif;font-size:17px;letter-spacing:0}
  .brand-dot{display:inline-block;width:14px;height:14px;border-radius:50%;background:var(--navy);margin-right:8px;vertical-align:2px}
  .brand-middle{left:0;top:95px;width:400px;text-align:center}
  .contact{position:absolute;left:0;top:225px;width:400px;text-align:center;font-family:"Open Sans",sans-serif;font-size:14px;color:var(--text);line-height:1.3}
  .contact-item{margin-bottom:22px}
  .contact-item svg{display:block;margin:0 auto 8px}
  .site{position:absolute;left:0;width:400px;text-align:center;font-family:"Libre Baskerville",serif;font-weight:700;font-size:13px;color:var(--white);letter-spacing:.3px}
  .site-middle{top:905px}

  /* right flap */
  .brand-right{left:32px;top:290px}
  .brand-right .brand-name{font-size:23px}
  .brand-right .brand-sub{font-size:14px}
  .offer{position:absolute;left:32px;top:420px;width:360px;color:var(--navy)}
  .offer-lead{font-family:"Roboto Condensed",sans-serif;font-size:42px;line-height:1}
  .offer-main{font-family:"Roboto Condensed",sans-serif;font-weight:700;font-size:60px;line-height:1.05;letter-spacing:-.5px}
  .offer-detail{font-family:"Poppins",sans-serif;font-size:19px;color:var(--text)}
  .offer-rule{width:118px;height:3px;background:var(--navy);margin:16px 0 12px}
  .offer-steps{font-family:"Roboto Condensed",sans-serif;font-weight:700;font-size:40px;line-height:1}
  .offer-list{font-family:"Open Sans",sans-serif;font-size:13.5px;color:var(--text);margin-top:8px;line-height:1.35}
  .site-right{top:935px}
</style>
</head>
<body>
<main class="flyer">

  <svg class="flyer-bg" viewBox="0 0 1200 970">
    <defs>
      <linearGradient id="waveTone" x1="0" y1="0" x2="1" y2="0">
        <stop offset="0" stop-color="#1d5fb8"/><stop offset=".5" stop-color="#232a86"/><stop offset="1" stop-color="#1d4fb0"/>
      </linearGradient>
      <linearGradient id="badgeFill" x1="0" y1="0" x2="1" y2="1">
        <stop offset="0" stop-color="#1c5cb6"/><stop offset="1" stop-color="#262a84"/>
      </linearGradient>
      <linearGradient id="coupleTone" x1="0" y1="0" x2="1" y2="1">
        <stop offset="0" stop-color="#fbf6ee"/><stop offset=".5" stop-color="#e6c9a8"/><stop offset="1" stop-color="#8fb0d8"/>
      </linearGradient>
      <linearGradient id="capsuleTone" x1="0" y1="0" x2="1" y2="1">
        <stop offset="0" stop-color="#fff4d6"/><stop offset=".6" stop-color="#f0b42a"/><stop offset="1" stop-color="#c27a06"/>
      </linearGradient>
      <linearGradient id="athleteTone" x1="0" y1="0" x2="0" y2="1">
        <stop offset="0" stop-color="#e3e6ea"/><stop offset=".55" stop-color="#9a9ea4"/><stop offset="1" stop-color="#5d6066"/>
      </linearGradient>
      <linearGradient id="sleepTone" x1="0" y1="0" x2="1" y2="1">
        <stop offset="0" stop-color="#f4f4f6"/><stop offset=".5" stop-color="#e2c2a8"/><stop offset="1" stop-color="#f7f7f9"/>
      </linearGradient>
      <clipPath id="leftPanel"><rect x="0" y="0" width="400" height="970"/></clipPath>
    </defs>

    <rect x="0" y="0" width="1200" height="970" fill="var(--paper)"/>
    <rect x="800" y="0" width="400" height="970" fill="var(--grey)"/>

    <!-- continuous blue swoosh and dark band -->
    <path d="M0,311 C170,285 330,350 420,455 C540,590 660,700 800,760 C920,800 1080,775 1200,720 L1200,970 L0,970 Z" fill="url(#waveTone)"/>
    <path d="M0,372 C150,340 300,390 400,485 C520,605 650,745 800,820 C920,870 1060,905 1200,925 L1200,970 L0,970 Z" fill="var(--dark)"/>

    <!-- left flap imagery -->
    <g clip-path="url(#leftPanel)">
      <circle cx="100" cy="880" r="300" fill="var(--bright)"/>
      <circle cx="92" cy="880" r="286" fill="url(#coupleTone)" role="img" aria-label="Photo of a smiling mature couple embracing outdoors"/>
    </g>
    <circle cx="206" cy="470" r="138" fill="var(--bright)"/>
    <circle cx="206" cy="470" r="130" fill="var(--white)"/>
    <circle cx="206" cy="470" r="125" fill="url(#badgeFill)"/>

    <!-- middle flap imagery -->
    <circle cx="606" cy="680" r="168" fill="var(--navy)"/>
    <circle cx="606" cy="680" r="156" fill="var(--white)"/>
    <circle cx="606" cy="680" r="150" fill="url(#athleteTone)" role="img" aria-label="Photo of a woman in a hooded top holding a green smoothie"/>
    <circle cx="487" cy="537" r="72" fill="#e6e6ea"/>
    <circle cx="487" cy="537" r="66" fill="url(#capsuleTone)" role="img" aria-label="Photo of golden supplement softgel capsules"/>

    <!-- right flap imagery -->
    <path d="M862,0 C910,150 1060,238 1200,238 L1200,205 C1065,200 935,130 885,0 Z" fill="var(--navy)"/>
    <path d="M885,0 L1200,0 L1200,205 C1065,200 935,130 885,0 Z" fill="url(#sleepTone)" role="img" aria-label="Photo of a woman sleeping peacefully on a white pillow"/>
    <circle cx="886" cy="99" r="50" fill="url(#waveTone)"/>
    <circle cx="925" cy="128" r="14" fill="var(--navy)"/>
  </svg>

  <!-- Flap: patient platform -->
  <section class="panel panel-left">
    <div class="platform-intro">
      <h2 class="platform-title">Computer platform</h2>
      <p class="platform-sub">TO MANAGE PATIENTS</p>
      <div class="title-rule"></div>
      <p class="platform-copy">Lorem ipsum dolor sit amet, consectetuer adipiscing elit, sed diam nonummy nibh euismod tincidunt ut laoreet dolore magna aliquam erat volutpat.</p>
      <p class="feature"><span class="feature-title">LOREM IPSUM</span>Lorem ipsum dolor sit amet, consectetuer adipiscing.</p>
    </div>
    <p class="gap-callout"><strong>FILL<br>NUTRITIONAL</strong><br>gaps that can<br>lead to a<br><strong>HORMONE<br>IMBALANCE.</strong></p>
  </section>

  <!-- Flap: contact -->
  <section class="panel panel-middle">
    <p class="brand brand-middle"><span class="brand-name"><span class="brand-dot"></span>VITALIS</span><span class="brand-sub">Wellness Solutions</span></p>
    <div class="contact">
      <div class="contact-item">
        <svg width="22" height="22" viewBox="0 0 24 24" fill="none" stroke="var(--navy)" stroke-width="2"><path d="M12 22s7-7 7-12a7 7 0 0 0-14 0c0 5 7 12 7 12z"/><circle cx="12" cy="10" r="2.5"/></svg>
        123 Lorem Ipsum Street,<br>magna aliquam volutpat. 145781
      </div>
      <div class="contact-item">
        <svg width="22" height="22" viewBox="0 0 24 24" fill="none" stroke="var(--navy)" stroke-width="2"><circle cx="12" cy="12" r="10"/><path d="M8 7l2 0 1 3-1.5 1a6 6 0 0 0 3 3l1-1.5 3 1 0 2a1.5 1.5 0 0 1-1.5 1.5A9 9 0 0 1 6.5 8.5 1.5 1.5 0 0 1 8 7z"/></svg>
        +14 5300 2196
      </div>
      <div class="contact-item">
        <svg width="22" height="22" viewBox="0 0 24 24" fill="none" stroke="var(--navy)" stroke-width="2"><circle cx="12" cy="12" r="10"/><rect x="6.5" y="8.5" width="11" height="7" rx="1"/><path d="M6.5 9l5.5 4 5.5-4"/></svg>
        info@VitalisWellness
      </div>
    </div>
    <p class="site site-middle">www.VitalisWellness.com</p>
  </section>

  <!-- Flap: recommendations cover -->
  <section class="panel panel-right">
    <p class="brand brand-right"><span class="brand-name"><span class="brand-dot"></span>VITALIS</span><span class="brand-sub">Wellness Solutions</span></p>
    <div class="offer">
      <p class="offer-lead">GET YOUR</p>
      <p class="offer-main">CUSTOMIZED</p>
      <p class="offer-detail">Supplement Recommendations</p>
      <div class="offer-rule"></div>
      <p class="offer-steps">IN 3 EASY STEPS</p>
      <p class="offer-list">Select Gender | Select Medical Conditions<br>Enter Your Current Medications</p>
    </div>
    <p class="site site-right">www.VitalisWellness.com</p>
  </section>

</main>
</body>
</html>
```